Company brochure for our unique consulting business

We are a small consulting business offering a unique set of services to our clients.. In simple terms we are a business improvement consultancy helping our clients get the best out of their businesses. We work with clients across multiple sectors and deliver a variety of services. We want to put together a brochure to cover these main themes:1. Who we are2. What we do3. The type of people we employ4. The sectors we work inWhile the brochure needs to have a certain corporate feel to it, we don't want it to be "boring" or "stiff". We would like it to have a slightly "friendly" or "informal" feel to it, to reflect the type of organisation we are.We have a company website http://tollandvergeadvisory.com , however we do not want to directly replicate the content or feel as we recognise it needs updating.We would like the brochure to be A4 portrait format. We anticipate requiring 12 sides (including covers) but we are happy to be guided on this based on the content we have provided.The attached ppt file gives the detail of the content to be included and also shows the proposed pagination. For the front cover we would like to try 2 versions, one with the TVA logo and one with the Tolland Verge Advisory logo (a file of both is attached)One of the most important pages will be the "Our Services" page. We would like this to cover the centre fold. In the ppt file we have shown an example layout, but this is where we need most help - we are clearly not graphic designers! This page will be the most used page in sales meetings etc.Also attached is the following:1. file for our TollandVerge Advisory company logo.2. File for our TVA company logo3. Files for Derek's signatures (for under photos) - Owen's to follow4. Photo of Derek & Owen (person in purple shirt to be cropped out)Thank you and really excited to see what everyone comes back with.Derek & Owen

Target Market(s)

Very broad - Manufacturing, Healthcare, Hospitality

Industry/Entity Type

Management Consulting

Font styles to use
Other font styles liked:
• We use Swiss721, but happy to be guided by designer

Colors
3276b5
85abd2
0355a3
333333
5c5c5c
9d9d9d
d9d9d9

Requirements
Must have
• Corporate feel
Nice to have
• Slightly friendly feel
• Our standard "blue" is (CORRECTION) - R55 G96 B146 #376092 and our standard grey is R197 G178, B179 - #B3B2B2, which we would like to keep, but other colours we are happy to be guided on. Brand guidelines attached.

```html
<!DOCTYPE html>
<html lang="en">
<head>
<meta charset="utf-8">
<title>Tolland Verge Advisory – Our People &amp; Quotes</title>
<link href="https://fonts.googleapis.com/css2?family=Source+Sans+3:ital,wght@0,200;0,300;0,400;0,600;1,400;1,700&display=swap" rel="stylesheet">
<style>
  :root {
    --backdrop: #e4e4e4;
    --paper: #fbfbfb;
    --brand-blue: #376092;
    --quote-blue: #2f5f9c;
    --heading-red: #8c2226;
    --ink: #1e1e1e;
    --ink-soft: #333333;
  }
  * { margin: 0; padding: 0; box-sizing: border-box; }
  html, body {
    width: 1200px; height: 960px; overflow: hidden;
    background: var(--backdrop);
    font-family: "Source Sans 3", "Helvetica Neue", Arial, sans-serif;
  }
  .spread {
    position: absolute; left: 20px; top: 63px;
    width: 1160px; height: 834px;
    background: var(--paper);
    box-shadow: 0 4px 14px rgba(0,0,0,0.12);
    overflow: hidden;
  }
  .spread::after {
    content: ""; position: absolute; top: 0; bottom: 0; left: 560px; width: 40px;
    background: linear-gradient(90deg, rgba(0,0,0,0) 0%, rgba(0,0,0,0.06) 50%, rgba(0,0,0,0) 100%);
    pointer-events: none;
  }
  .hero-photo {
    position: absolute; left: 0; top: 0; width: 1160px; height: 336px;
    background:
      radial-gradient(ellipse 260px 180px at 690px 150px, rgba(255,226,170,0.85), rgba(255,240,210,0) 70%),
      linear-gradient(180deg, #dfe4e6 0%, #eef0ef 45%, #c9ccd0 62%, #eeeeee 80%, #f6f6f6 100%);
  }
  .section-title {
    position: absolute; left: 771px; top: 120px;
    font-weight: 200; font-size: 66px; line-height: 1; color: #ffffff;
    letter-spacing: 0.5px;
  }
  .title-rule {
    position: absolute; left: 1003px; top: 165px; width: 114px; height: 1px;
    background: rgba(255,255,255,0.9);
  }
  .accent-bar {
    position: absolute; left: 0; top: 377px; width: 20px; height: 52px;
    background: var(--brand-blue);
  }
  .page-heading {
    position: absolute; left: 41px; top: 373px;
    font-weight: 300; font-size: 33px; line-height: 1.1; color: var(--heading-red);
  }
  .body-copy {
    position: absolute; left: 315px; top: 378px; width: 238px;
    font-size: 12.3px; line-height: 17.3px; color: var(--ink-soft);
  }
  .body-copy p + p { margin-top: 17.3px; }
  .quote-column {
    position: absolute; top: 378px; width: 232px;
    font-size: 12.3px; line-height: 17.3px;
  }
  .quote-column.first { left: 626px; }
  .quote-column.second { left: 892px; }
  .testimonial + .testimonial { margin-top: 35px; }
  .testimonial blockquote { color: var(--quote-blue); }
  .testimonial .role { font-style: italic; font-weight: 700; color: var(--ink); }
  .testimonial .org { font-style: italic; color: var(--ink-soft); }
</style>
</head>
<body>
  <main class="spread">
    <div class="hero-photo" role="img" aria-label="Blurred crowd of business people walking through a bright glass-walled lobby"></div>
    <h2 class="section-title">Quotes</h2>
    <div class="title-rule"></div>

    <div class="accent-bar"></div>
    <h1 class="page-heading">OUR PEOPLE</h1>

    <section class="body-copy">
      <p>All of our team at TVA started their careers in operational roles. This means we understand what it’s like to be in your shoes. Blending this understanding with our years of experience and skills we are able to work in partnership with you and your teams to deliver great results, together. Simply put, our team has some of the best people in the industry.</p>
      <p>We also recognise no single person knows everything, so within the team we have experts in their own fields. They are able to bring their specialised skills and experience, at the right time and in the best way possible.</p>
      <p>Our team also understand the importance of engagement. Everyone in your team will get to know us on first name terms, because we take the time to listen to everyone, from shop floor to senior management</p>
    </section>

    <section class="quote-column first">
      <figure class="testimonial">
        <blockquote>TVA have achieved excellent engagement throughout the entire organisation with significant measurable successes.</blockquote>
        <figcaption><div class="role">Director of Operations</div><div class="org">KLR</div></figcaption>
      </figure>
      <figure class="testimonial">
        <blockquote>With the team from TVA we have been able to embed an improvement approach across the entire organisation.</blockquote>
        <figcaption><div class="role">Chief Operations Officer</div><div class="org">Fairmead Hospital</div></figcaption>
      </figure>
      <figure class="testimonial">
        <blockquote>You have definitely made our lives easier knowing that you are taking care of our British colleagues. If we have future needs, we will definitely be straight back to you.</blockquote>
        <figcaption><div class="role">Chief Operations Officer</div><div class="org">Harbourline Games</div></figcaption>
      </figure>
    </section>

    <section class="quote-column second">
      <figure class="testimonial">
        <blockquote>The team from TVA have been invaluable with helping implement our lean programme. They’ve helped break down what seemed very complicated at the start, into logical and simple steps.</blockquote>
        <figcaption><div class="role">Managing Director</div><div class="org">Penrose Supplies</div></figcaption>
      </figure>
      <figure class="testimonial">
        <blockquote>TVA have been able offer us support across a range of topics based on their in-depth knowledge of lean and Tamura systems</blockquote>
        <figcaption><div class="role">Continuous Improvement Manager</div><div class="org">Holtmann Motors</div></figcaption>
      </figure>
    </section>
  </main>
</body>
</html>
```